Brochure for Adult Skin Care Products
Velo-Sana Brochure
Brochure for Adult Skin Care Products - Personal Care
Creative Brief
Personal Care
Adults, but not just elderly. Care givers for older people. And business to business retailers.
The brochure will be a 8 1/2 x 11 in. trifold brochure, 4 color, ready to send to printer.

```html
<!DOCTYPE html>
<html lang="en">
<head>
<meta charset="utf-8">
<title>Velo-Sana Trifold Brochure</title>
<link href="https://fonts.googleapis.com/css2?family=Open+Sans:wght@400;600;700&display=swap" rel="stylesheet">
<style>
  :root{
    --stage:#d9d9dc;
    --charcoal:#2e2d33;
    --purple:#8657a6;
    --purple-dark:#5f3580;
    --lavender:#d8c8e8;
    --lavender-pale:#f3eef7;
    --yellow:#e4da1c;
    --lime:#c9d63a;
    --orange:#ee8a2a;
    --peach:#f2c7a0;
    --mint:#cfe2a6;
    --ink:#4d4a52;
    --paper:#ffffff;
  }
  *{box-sizing:border-box;margin:0;padding:0}
  html,body{width:1200px;height:838px;overflow:hidden}
  body{background:var(--stage);font-family:"Open Sans",Arial,sans-serif;color:var(--ink)}
  .brochure{position:absolute;left:81px;top:17px;width:1038px;height:804px;display:flex;box-shadow:0 4px 18px rgba(0,0,0,.18)}
  .panel{position:relative;width:346px;height:804px;overflow:hidden;background:var(--paper)}
  .panel + .panel{border-left:1px solid #e6e2ea}
  .panel svg.shape{position:absolute;left:0;top:0}
  .body-text{position:absolute;font-size:12.5px;line-height:1.6}
  .body-text p + p{margin-top:12px}
  .body-text strong{color:var(--purple-dark)}

  /* left panel */
  .panel--about{background:var(--lavender-pale)}
  .about-brand{position:absolute;left:0;top:34px;width:346px;text-align:center}
  .about-brand .dot{display:block;width:46px;height:46px;border-radius:50%;background:var(--orange);margin:0 auto 10px}
  .about-brand .name{font-size:13px;font-weight:600;color:#f0edf3;letter-spacing:.5px}
  .panel--about .body-text{left:30px;top:178px;width:286px}
  .pattern-area{position:absolute;left:0;top:640px;width:346px;height:164px;background:linear-gradient(100deg,var(--peach) 0%,var(--lavender) 55%,var(--mint) 100%);opacity:.85}

  /* middle panel */
  .partner-brand{position:absolute;left:30px;top:36px;display:flex;align-items:center;gap:10px}
  .partner-brand .square{width:22px;height:22px;background:var(--orange)}
  .partner-brand .name{font-size:18px;font-weight:700;color:var(--purple-dark)}
  .panel--info .purple-text{left:34px;top:140px;width:278px;color:#fff}
  .panel--info .purple-text strong{color:var(--yellow)}
  .panel--info .lower-text{left:34px;top:520px;width:278px}

  /* cover panel */
  .cover-logo{position:absolute;left:118px;top:22px;width:110px;height:110px;border-radius:50%;background:var(--lime);border:4px solid var(--purple);display:flex;flex-direction:column;align-items:center;justify-content:center}
  .cover-logo .name{font-size:17px;font-weight:700;color:var(--purple-dark)}
  .cover-logo .tag{font-size:9px;color:var(--purple-dark);margin-top:2px}
  .product-shot{position:absolute;left:150px;top:150px;width:180px;height:120px;background:linear-gradient(135deg,#f7f5fa,#cfc0df)}
  .tagline{position:absolute;left:18px;top:162px;width:128px;color:var(--purple-dark)}
  .tagline h2{font-size:15px;line-height:1.25;font-weight:700}
  .tagline p{font-size:11px;line-height:1.4;margin-top:8px}
  .lifestyle-photo{position:absolute;left:0;top:290px;width:346px;height:220px;background:linear-gradient(160deg,#dfe9f2 0%,#b9c9a0 55%,#8a9a6a 100%)}
  .agency{position:absolute;left:0;top:560px;width:346px;text-align:center}
  .agency .mark{display:inline-block;width:16px;height:16px;background:#d2232a;vertical-align:middle;margin-right:8px}
  .agency .name{font-size:16px;font-weight:700;color:var(--charcoal);vertical-align:middle}
  .contact{position:absolute;left:40px;top:620px;width:266px;text-align:center;font-size:11.5px;line-height:1.6}
  .contact .lead{font-weight:600;color:var(--purple-dark);margin-bottom:6px}
</style>
</head>
<body>
<main class="brochure">

  <section class="panel panel--about">
    <svg class="shape" width="346" height="804" viewBox="0 0 346 804">
      <path d="M0 0H346V130C250 160 110 155 0 140Z" fill="var(--charcoal)"/>
    </svg>
    <div class="about-brand">
      <span class="dot"></span>
      <span class="name">Brightleaf Wellness Inc.</span>
    </div>
    <div class="body-text">
      <p>Our team has spent over twenty years helping adults and their care givers find gentle, dependable products for daily skin comfort. Every item we carry is tested for sensitive skin and chosen with real routines in mind.</p>
      <p>We work closely with retailers, clinics and home care providers to keep shelves stocked and customers confident. Ask about volume pricing and our partner program.</p>
      <p><strong>Call us today to learn more.</strong></p>
    </div>
    <div class="pattern-area" role="img" aria-label="Decorative pastel bubble pattern in peach, lavender and mint"></div>
  </section>

  <section class="panel panel--info">
    <svg class="shape" width="346" height="804" viewBox="0 0 346 804">
      <path d="M0 105C120 85 240 90 346 112V470C230 500 110 490 0 460Z" fill="var(--purple)"/>
      <path d="M0 470C110 500 230 510 346 480V498C230 528 110 518 0 488Z" fill="var(--yellow)"/>
      <path d="M0 92C120 72 240 78 346 98V106C240 86 120 80 0 100Z" fill="var(--yellow)"/>
      <path d="M346 700C280 720 220 770 200 804H260C280 770 310 745 346 735Z" fill="var(--yellow)"/>
      <path d="M346 745C310 760 290 785 285 804H346Z" fill="var(--purple)"/>
    </svg>
    <div class="partner-brand">
      <span class="square"></span>
      <span class="name">Harlow Solutions Inc.</span>
    </div>
    <div class="body-text purple-text">
      <p>Velo-Sana cleansers and creams are designed for skin that needs extra care. Mild formulas clean without rinsing, soothe dryness and help protect against irritation through the day and night.</p>
      <p><strong>Ideal for home use, assisted living and hospital settings.</strong></p>
    </div>
    <div class="body-text lower-text">
      <p>Each product is fragrance light, pH balanced and easy to use, so care givers can spend less time on routines and more time with the people they love.</p>
      <p><strong>Simple care, every single day.</strong></p>
    </div>
  </section>

  <section class="panel panel--cover">
    <svg class="shape" width="346" height="804" viewBox="0 0 346 804">
      <rect width="346" height="290" fill="var(--lavender-pale)"/>
      <path d="M0 0H346V60C260 30 150 120 0 90Z" fill="var(--purple)"/>
      <path d="M0 90C150 120 260 30 346 60V72C260 44 150 134 0 104Z" fill="var(--yellow)"/>
      <rect y="510" width="346" height="10" fill="var(--yellow)"/>
      <path d="M0 520H346V532C230 548 110 546 0 530Z" fill="var(--purple)"/>
    </svg>
    <div class="cover-logo">
      <span class="name">Velo-Sana</span>
      <span class="tag">Adult Skin Care</span>
    </div>
    <div class="tagline">
      <h2>One Daily Solution for Gentle Skin Care</h2>
      <p>Trusted by families and care givers alike</p>
    </div>
    <div class="product-shot" role="img" aria-label="Product photo of white Velo-Sana skin care bottles"></div>
    <div class="lifestyle-photo" role="img" aria-label="Photo of an older couple riding bicycles outdoors"></div>
    <div class="agency">
      <span class="mark"></span><span class="name">Northfield Health Agency</span>
    </div>
    <div class="contact">
      <p class="lead">For more information on our products contact:</p>
      <p>1440 Maple Grove Road, Suite 12</p>
      <p>Ashford, ON K7L 2P4</p>
      <p>Phone 1 800 555 0142 | info@velosana.example</p>
    </div>
  </section>

</main>
</body>
</html>
```